quorvel stationary business card and letterhead

THIS PROJECT IS TO DESIGN A BUSINESS CARD DOUBLE SIDES .

Reason: I AM WAITING FOR BEZITH SUBMISION

Industry/Entity Type

Business

Font styles to use
Other font styles liked:
• Chose your font

```html
<!DOCTYPE html>
<html lang="en">
<head>
<meta charset="utf-8">
<title>Quorvel Business Card</title>
<link rel="stylesheet" href="https://fonts.googleapis.com/css2?family=Cinzel:wght@400;600&family=Questrial&display=swap">
<style>
  :root {
    --yellow: #f2bb12;
    --yellow-deep: #e3a90a;
    --ink: #1b1a18;
    --paper: #f7f7f7;
    --paper-shade: #ececec;
    --grey-text: #4a4a4a;
    --backdrop: #d9d9d9;
  }
  * { margin: 0; padding: 0; box-sizing: border-box; }
  html, body { width: 1200px; height: 840px; overflow: hidden; }
  body {
    background: var(--backdrop);
    font-family: "Questrial", sans-serif;
    position: relative;
  }
  .card {
    position: absolute;
    left: 250px;
    width: 700px;
    height: 400px;
    overflow: hidden;
    box-shadow: 0 6px 18px rgba(0,0,0,0.18);
  }
  .card-front { top: 14px; background: var(--paper); }
  .card-back { top: 426px; background: var(--ink); }

  .front-shade {
    position: absolute;
    top: 0; right: 0;
    width: 310px; height: 100%;
    background: var(--paper-shade);
  }
  .logo-band {
    position: absolute;
    left: 0; top: 82px;
    width: 92px; height: 54px;
    background: var(--yellow);
  }
  .logo {
    position: absolute;
    display: flex;
    align-items: center;
    gap: 10px;
  }
  .card-front .logo { left: 70px; top: 80px; }
  .logo-dot {
    width: 58px; height: 58px;
    border-radius: 50%;
    background: var(--ink);
    border: 6px solid var(--yellow);
    flex: none;
  }
  .logo-name {
    font-family: "Cinzel", serif;
    font-weight: 600;
    font-size: 40px;
    letter-spacing: 1px;
    color: var(--ink);
    line-height: 1;
  }
  .logo-tagline {
    font-family: "Cinzel", serif;
    font-size: 14px;
    letter-spacing: 1px;
    color: var(--yellow);
    margin-top: 4px;
  }
  .person {
    position: absolute;
    right: 30px; top: 84px;
    width: 270px;
    text-align: right;
  }
  .person-name {
    font-family: "Cinzel", serif;
    font-size: 30px;
    color: var(--grey-text);
    letter-spacing: 2px;
    padding-right: 40px;
  }
  .person-rule {
    height: 3px;
    background: var(--yellow);
    margin: 6px 0 6px;
  }
  .person-role {
    font-family: "Cinzel", serif;
    font-size: 19px;
    color: var(--ink);
    padding-right: 48px;
  }
  .contact-bar {
    position: absolute;
    left: 0; bottom: 0;
    width: 100%; height: 62px;
    background: linear-gradient(90deg, var(--yellow), var(--yellow-deep));
    display: flex;
    align-items: center;
    justify-content: space-between;
    padding: 0 30px 0 40px;
  }
  .contact {
    display: flex;
    align-items: center;
    gap: 10px;
    font-size: 15px;
    letter-spacing: 1.5px;
    color: var(--ink);
  }
  .contact-icon {
    width: 28px; height: 28px;
    border-radius: 50%;
    background: var(--ink);
    border: 2px solid #ffffff;
    flex: none;
    display: flex; align-items: center; justify-content: center;
  }
  .back-art { position: absolute; inset: 0; }
  .card-back .logo { left: 200px; top: 70px; }
  .card-back .logo-name { color: var(--paper); }
</style>
</head>
<body>
  <section class="card card-front">
    <div class="front-shade"></div>
    <div class="logo-band"></div>
    <div class="logo">
      <div class="logo-dot"></div>
      <div>
        <div class="logo-name">QUORVEL</div>
        <div class="logo-tagline">International Consulting</div>
      </div>
    </div>
    <div class="person">
      <div class="person-name">TAVRIN</div>
      <div class="person-rule"></div>
      <div class="person-role">IT Support</div>
    </div>
    <div class="contact-bar">
      <div class="contact"><span class="contact-icon"></span>tavrin@quorvel-mail.com</div>
      <div class="contact"><span class="contact-icon"></span>tavrin@quorvel-mail.com</div>
      <div class="contact">
        <span class="contact-icon">
          <svg width="14" height="14" viewBox="0 0 24 24"><path fill="#ffffff" d="M6.6 10.8c1.4 2.8 3.8 5.1 6.6 6.6l2.2-2.2c.3-.3.7-.4 1-.2 1.1.4 2.3.6 3.6.6.6 0 1 .4 1 1V20c0 .6-.4 1-1 1C10.6 21 3 13.4 3 4c0-.6.4-1 1-1h3.5c.6 0 1 .4 1 1 0 1.3.2 2.5.6 3.6.1.3 0 .7-.2 1z"/></svg>
        </span>0215-30417728
      </div>
    </div>
  </section>

  <section class="card card-back">
    <svg class="back-art" width="700" height="400" viewBox="0 0 700 400" aria-hidden="true">
      <path d="M0 250 C 180 190, 420 150, 700 110 L700 400 L0 400 Z" fill="var(--yellow)"/>
    </svg>
    <div class="logo">
      <div class="logo-dot"></div>
      <div>
        <div class="logo-name">QUORVEL</div>
        <div class="logo-tagline">International Consulting</div>
      </div>
    </div>
  </section>
</body>
</html>
```